vortane realty business card

We need a Business card for our new business. The logo was designed by ArtQuillo, and the text We want on the back is:
REAL ESTATE INVESTMENTS
- BUY, RENOVATE, SELL AND RENT RESIDENTIAL PROPERTIES
- FULL HOME REHABBING , REMODELING AND INTERIOR DESIGN
- HOME STAGING SERVICES
- WHOLESALE INVESTOR PROPERTIES
- MAKE CASH OFFERS ON HOUSES IN ANY CONDITION AND IN ANY SITUATION
- PRIVATE MONEY INVESTOR PROGRAMS WITH 6-12% RETURNS
- PAY CASH REWARDS FOR REFFERALS
- CONCIERGE SERVICE

```html
<!DOCTYPE html>
<html lang="en">
<head>
<meta charset="utf-8">
<title>Vortane Realty – Business Card</title>
<link rel="stylesheet" href="https://fonts.googleapis.com/css2?family=Ubuntu:wght@400;500;700&family=PT+Sans:wght@400&display=swap">
<style>
  :root{
    --page:#ebe8e4;
    --card:#ffffff;
    --grey:#8b8c8e;
    --grey-text:#7d7e80;
    --teal:#75c9dc;
    --white:#ffffff;
  }
  *{box-sizing:border-box;margin:0;padding:0}
  html,body{width:1200px;height:1000px;overflow:hidden}
  body{background:var(--page);position:relative;font-family:"Ubuntu",sans-serif}
  .card{position:absolute;left:265px;width:666px;height:397px;overflow:hidden;box-shadow:0 3px 10px rgba(0,0,0,.18)}
  .card--front{top:73px;background:var(--card)}
  .card--back{top:533px;background:var(--grey)}
  .abs{position:absolute}

  .brand{left:33px;top:64px;display:flex;align-items:center;gap:22px}
  .brand__mark{width:62px;height:74px;background:var(--teal)}
  .brand__name{font-size:38px;font-weight:400;color:var(--grey-text);letter-spacing:.5px;line-height:1}
  .brand__tagline{font-size:20px;color:var(--grey-text);letter-spacing:1.4px;margin-top:12px;line-height:1}

  .person{left:33px;top:221px}
  .person__name{font-size:27px;font-weight:500;color:var(--teal);line-height:1.1}
  .person__role{font-size:18px;color:var(--grey-text);line-height:1}
  .website{left:33px;top:330px;font-size:18px;font-weight:700;color:var(--teal)}

  .contact{left:334px;top:222px;font-size:17px;color:var(--grey-text);line-height:22.5px;letter-spacing:.3px}
  .contact__label{color:var(--teal);font-weight:700}
  .address{left:334px;top:308px;font-size:17px;color:var(--grey-text);line-height:22px;letter-spacing:.3px}

  .band{position:absolute;bottom:0;height:32px}
  .band--left{left:0;width:330px}
  .band--right{left:335px;right:0;background:var(--teal)}
  .card--front .band--left{background:var(--grey)}
  .card--back .band--left{background:var(--white);width:331px}

  .services{left:33px;top:97px;list-style:none;font-family:"PT Sans",sans-serif;font-size:15px;color:var(--white)}
  .services li{height:26px;display:flex;align-items:center;gap:7px}
  .services li::before{content:"";width:9px;height:9px;background:var(--teal);flex:none}
</style>
</head>
<body>
  <section class="card card--front">
    <div class="abs brand">
      <div class="brand__mark"></div>
      <div>
        <div class="brand__name">VORTANE REALTY</div>
        <div class="brand__tagline">REAL ESTATE SOLUTIONS</div>
      </div>
    </div>

    <div class="abs person">
      <div class="person__name">Daniel R Hale</div>
      <div class="person__role">Manager</div>
    </div>
    <div class="abs website">www.vortanerealty.com</div>

    <div class="abs contact">
      <div><span class="contact__label">Phone:</span> + 999 999 9999</div>
      <div><span class="contact__label">Fax:</span> + 999 999 9999</div>
      <div><span class="contact__label">Email:</span> daniel@vortanerealty.com</div>
    </div>
    <div class="abs address">
      <div>42 Ashgrove Lane, Brindlow</div>
      <div>Northamptonshire, NN9</div>
    </div>

    <div class="band band--left"></div>
    <div class="band band--right"></div>
  </section>

  <section class="card card--back">
    <ul class="abs services">
      <li>BUY, RENOVATE, SELL AND RENT RESIDENTIAL PROPERTIES</li>
      <li>FULL HOME REHABBING , REMODELING AND INTERIOR DESIGN</li>
      <li>HOME STAGING SERVICES</li>
      <li>WHOLESALE INVESTOR PROPERTIES</li>
      <li>MAKE CASH OFFERS ON HOUSES IN ANY CONDITION AND IN ANY SITUATION</li>
      <li>PRIVATE MONEY INVESTOR PROGRAMS WITH 6-12% RETURNS</li>
      <li>PAY CASH REWARDS FOR REFFERALS</li>
      <li>CONCIERGE SERVICE</li>
    </ul>
    <div class="band band--left"></div>
    <div class="band band--right"></div>
  </section>
</body>
</html>
```